Letterhead for a Natural Hair Run

We need a letterhead design with the logo uploaded entitled 'Bluevista Dash'. This run is a natural 5K run seeking to promote the acceptance of natural beauty in every aspect of society encompassing one's ethnic roots and its connection to a healthy lifetstyle. We would like to see designs coordinating with our logo. The design should be fun and exciting!

Industry/Entity Type

Hair

Font styles to use
Serif
Sans Serif

Requirements
Must have
• Please included this information on the letter head:
• P.O. Box K7214
• Port Lira, Marenas
• Phone: (242) 618-2097
• Email: goskyward517@mailbrisk.net

```html
<!DOCTYPE html>
<html lang="en">
<head>
<meta charset="utf-8">
<title>Bluevista Dash Letterhead</title>
<link href="https://fonts.googleapis.com/css2?family=Barlow:wght@300;400&display=swap" rel="stylesheet">
<style>
  :root {
    --aqua: #4cf7dc;
    --sun: #ffe629;
    --paper: #ffffff;
    --ink: #1b1b1b;
    --footer-ink: #2e2e2e;
    --art-deep: #3c3c3c;
    --art-soft: #8a8a8a;
  }
  html, body {
    margin: 0;
    padding: 0;
    overflow: hidden;
    background: var(--paper);
  }
  .letterhead {
    position: relative;
    width: 927px;
    height: 1200px;
    overflow: hidden;
    background: var(--paper);
    font-family: "Barlow", sans-serif;
  }
  .swooshes {
    position: absolute;
    inset: 0;
    width: 927px;
    height: 1200px;
  }
  .runners-art {
    position: absolute;
    left: 114px;
    top: 132px;
    width: 262px;
    height: 130px;
    border-radius: 6px;
    background: linear-gradient(180deg, var(--art-soft) 0%, var(--art-deep) 100%);
  }
  .brand-name {
    position: absolute;
    left: 114px;
    top: 266px;
    margin: 0;
    font-size: 31px;
    font-weight: 400;
    letter-spacing: 2.6px;
    color: var(--ink);
    line-height: 1;
    white-space: nowrap;
  }
  .contact-line {
    position: absolute;
    left: 86px;
    top: 1110px;
    margin: 0;
    font-size: 16.5px;
    font-weight: 300;
    color: var(--footer-ink);
    letter-spacing: 0.25px;
    white-space: nowrap;
  }
</style>
</head>
<body>
  <div class="letterhead">
    <svg class="swooshes" viewBox="0 0 927 1200" aria-hidden="true">
      <path fill="var(--aqua)" d="M0,0 H395 C250,40 95,200 0,393 Z"/>
      <path fill="var(--sun)" d="M450,0 H927 V184 C790,70 640,28 550,34 C340,46 160,180 55,325 C130,190 280,50 450,0 Z"/>
      <circle cx="232" cy="228" r="148" fill="var(--paper)"/>
      <path fill="none" stroke="var(--aqua)" stroke-width="2" d="M250,76 C300,82 330,100 340,118"/>
      <line x1="86" y1="1101" x2="832" y2="1101" stroke="var(--aqua)" stroke-width="1.2"/>
      <line x1="86" y1="1138" x2="790" y2="1138" stroke="var(--aqua)" stroke-width="1.2"/>
      <path fill="var(--aqua)" d="M894,1028 C860,1100 790,1160 690,1200 H720 C810,1160 875,1105 894,1028 Z"/>
      <path fill="var(--aqua)" d="M927,988 V1200 H740 C840,1155 905,1080 927,988 Z"/>
    </svg>

    <div class="runners-art" role="img" aria-label="Illustration area: a family of runners shown in silhouette"></div>
    <p class="brand-name">Bluevista Dash</p>

    <p class="contact-line">P.O. Box K7214 | Port Lira, Marenas | Phone: (242) 618-2097 | Email: goskyward517@mailbrisk.net</p>
  </div>
</body>
</html>
```